One of Australia's fastest growing Financial Company looking for an updated business card design!

Meridale Partners Australia is looking for an updated design for our business cards. We would like to keep up our professional appearances and have get new exciting design that fits our company.

The Meridale aim is to facilitate and assist clients in every financial requirement that may arise in financial areas.

We would to see the design to use colour blue and we like the clouds in the background. We have attached two designs we have use before but we need something with more professional and easy to read design.

We would like the website in the back of the card; the employees name more central and stands out; only a postal address; a list of all our locations along the bottom (Sydney, Melbourne, Brisbane, Singapore)

Looking forward to seeing the designs come in!

Target Market(s)

Other Industry Professionals
Middle Class Families

Industry/Entity Type

Finance

Contact Information for Business Card

Name; Company Role; Office Number; Mobile Number; Email Address; Website; Postal Address; Locations

Font styles to use
Serif
Sans Serif

Colors
0492cd
33a6d7
85cae6
85acd3
3176b5
0455a3
cee9f5
d5e2ee

Requirements
Must have
• Name; Company Role; Office Number; Mobile Number; Email Address; Website; Postal Address; Locations
Nice to have
• The colour blue, clouds on the background

```html
<!DOCTYPE html>
<html lang="en">
<head>
<meta charset="utf-8">
<title>Meridale Partners Australia – Business Card</title>
<link rel="stylesheet" href="https://fonts.googleapis.com/css2?family=Lato:wght@400;700&display=swap">
<style>
  :root {
    --page-bg: #e9e8ea;
    --navy: #0455a3;
    --navy-deep: #0b3f8c;
    --mid-blue: #3176b5;
    --sky: #85acd3;
    --cloud-white: #f7f8fa;
    --cloud-grey: #d5e2ee;
    --white: #ffffff;
  }
  * { box-sizing: border-box; margin: 0; padding: 0; }
  html, body {
    width: 1200px; height: 800px; overflow: hidden;
    background: var(--page-bg);
    font-family: "Lato", Arial, sans-serif;
  }
  .sheet {
    position: relative; width: 1200px; height: 800px;
    display: flex; align-items: center; justify-content: center; gap: 50px;
  }
  .card {
    position: relative; width: 525px; height: 300px; overflow: hidden;
    background: var(--white);
    box-shadow: 0 6px 18px rgba(40, 50, 70, 0.18);
  }

  /* Front */
  .card-front__sky {
    position: absolute; inset: 0 0 66px 0;
    background:
      radial-gradient(ellipse at 30% 85%, rgba(11,63,140,0.9), transparent 60%),
      radial-gradient(ellipse at 75% 20%, rgba(49,118,181,0.5), transparent 55%),
      linear-gradient(160deg, var(--navy) 0%, var(--navy-deep) 100%);
  }
  .card-front__content {
    position: absolute; inset: 0 0 66px 0;
    display: flex; align-items: center; justify-content: center;
    color: var(--white);
  }
  .identity { text-align: right; padding-right: 16px; }
  .identity__name {
    font-size: 44px; font-weight: 700; line-height: 1; letter-spacing: 0.5px;
    display: flex; align-items: center; justify-content: flex-end; gap: 10px;
  }
  .identity__dot {
    width: 18px; height: 18px; border-radius: 50%; background: var(--white);
  }
  .identity__contact { margin-top: 10px; font-size: 13px; line-height: 1.45; }
  .divider { width: 1.5px; height: 104px; background: var(--white); }
  .person { padding-left: 16px; }
  .person__service { font-size: 14px; }
  .person__name { font-size: 19px; font-weight: 700; margin-top: 2px; white-space: nowrap; }
  .person__role { font-size: 12px; font-weight: 400; }
  .person__phones { margin-top: 10px; font-size: 14px; line-height: 1.35; }

  .card-front__footer {
    position: absolute; left: 0; right: 0; bottom: 0; height: 66px;
    display: flex; flex-direction: column; align-items: center; justify-content: center; gap: 5px;
    color: var(--navy);
  }
  .card-front__address { font-size: 15px; font-weight: 700; letter-spacing: 0.3px; }
  .locations {
    display: flex; gap: 10px; list-style: none;
    font-size: 11px; font-weight: 400; letter-spacing: 1.2px; text-transform: uppercase;
    color: var(--mid-blue);
  }
  .locations li + li::before { content: "•"; margin-right: 10px; color: var(--sky); }

  /* Back */
  .card-back__clouds {
    position: absolute; inset: 0;
    background:
      radial-gradient(ellipse at 20% 80%, var(--white), transparent 55%),
      radial-gradient(ellipse at 80% 30%, var(--cloud-white), transparent 60%),
      linear-gradient(180deg, var(--cloud-grey) 0%, var(--cloud-white) 55%, #e4ebf3 100%);
  }
  .card-back__content {
    position: absolute; inset: 0;
    display: flex; flex-direction: column; align-items: center; justify-content: center; gap: 14px;
    color: var(--navy);
  }
  .card-back__mark {
    display: flex; align-items: center; gap: 14px;
    font-size: 64px; font-weight: 700; line-height: 1; letter-spacing: 0.5px;
  }
  .card-back__dot {
    width: 28px; height: 28px; border-radius: 50%; background: var(--navy);
  }
  .card-back__website { font-size: 15px; font-weight: 700; letter-spacing: 0.3px; }
</style>
</head>
<body>
<main class="sheet">
  <section class="card card-front">
    <div class="card-front__sky" role="img" aria-label="Deep blue cloudy sky background"></div>
    <div class="card-front__content">
      <div class="identity">
        <div class="identity__name"><span class="identity__dot"></span>Meridale</div>
        <div class="identity__contact">d.rowe@meridale.com.au</div>
      </div>
      <div class="divider"></div>
      <div class="person">
        <div class="person__service">Premium Bank Services</div>
        <div class="person__name">Daniel Rowe / <span class="person__role">Manager</span></div>
        <div class="person__phones">02 9412 7300<br>0412 558 190</div>
      </div>
    </div>
    <div class="card-front__footer">
      <div class="card-front__address">PO Box 418, Parramatta NSW 2150</div>
      <ul class="locations">
        <li>Sydney</li>
        <li>Melbourne</li>
        <li>Brisbane</li>
        <li>Singapore</li>
      </ul>
    </div>
  </section>

  <section class="card card-back">
    <div class="card-back__clouds" role="img" aria-label="Soft white clouds background"></div>
    <div class="card-back__content">
      <div class="card-back__mark"><span class="card-back__dot"></span>Meridale</div>
      <div class="card-back__website">www.MeridalePartnersAustralia.com.au</div>
    </div>
  </section>
</main>
</body>
</html>
```